Business Card Design for Photographer

Updating business card design. Must use included logo. We're a luxury wedding photography business. Elegancy, luxury, consistency are messages we wish to convey.

Visit our website at www.colbyvarnway.com to familiarize yourself more with our brand design currently (fonts, colors etc.). This is what we want to maintain.

Target Market(s)

Luxury Brides and Grooms

Industry/Entity Type

Wedding

Contact Information for Business Card

Current logo (attached to brief)
Name: Colby Varnway
Phone: 5208813047
website/blog
Email

Requirements
Must have
• Current logo (attached to brief)
• Name: Colby Varnway
• Phone: 5208813047
• website/blog
• Email
• Instagram username
Should not have
• bright colors, fonts that don't suit our brand (visit www.colbyvarnway.com)

```html
<!DOCTYPE html>
<html lang="en">
<head>
<meta charset="utf-8">
<title>Colby Varnway Photographers – Business Card</title>
<link href="https://fonts.googleapis.com/css2?family=Tenor+Sans&family=Crimson+Text&display=swap" rel="stylesheet">
<style>
  :root {
    --backdrop: #e9e7e4;
    --card-white: #ffffff;
    --brand-grey: #717372;
    --ink-grey: #6a6a6a;
    --rule-grey: #7a7a7a;
    --on-grey: #ffffff;
  }
  html, body { margin: 0; padding: 0; overflow: hidden; }
  body { width: 1200px; height: 1000px; background: var(--backdrop); position: relative; }

  .card { position: absolute; left: 265px; width: 665px; height: 397px; box-shadow: 0 4px 14px rgba(0,0,0,.18); }
  .card-front { top: 73px; background: var(--card-white); }
  .card-back { top: 532px; background: var(--brand-grey); }
  .front-band { position: absolute; left: 0; right: 0; bottom: 0; height: 32px; background: var(--brand-grey); }

  .brand-mark { position: absolute; background: var(--ink-grey); }
  .brand-name, .brand-tagline {
    position: absolute; margin: 0; font-family: "Tenor Sans", sans-serif; font-weight: 400;
    text-transform: uppercase; white-space: nowrap; text-align: center; color: var(--ink-grey);
  }

  .card-front .brand-mark { left: 166px; top: 124px; width: 56px; height: 58px; }
  .card-front .brand-name { left: 20px; width: 348px; top: 205px; font-size: 26px; letter-spacing: 3.2px; }
  .card-front .brand-tagline { left: 20px; width: 348px; top: 246px; font-size: 14px; letter-spacing: 5px; }

  .divider { position: absolute; left: 389px; top: 124px; width: 2px; height: 137px; background: var(--rule-grey); }

  .contact { position: absolute; left: 421px; top: 120px; font-family: "Crimson Text", serif; color: var(--ink-grey); }
  .contact-name { margin: 0 0 22px; font-size: 21px; font-weight: 400; }
  .contact-list { list-style: none; margin: 0; padding: 0; font-size: 16px; }
  .contact-list li { display: flex; align-items: center; height: 21px; }
  .contact-list li.social { margin-top: 6px; }
  .contact-list svg { width: 12px; height: 12px; margin-right: 7px; fill: var(--ink-grey); flex: none; }

  .card-back .brand-mark { background: var(--on-grey); left: 296px; top: 96px; width: 72px; height: 72px; }
  .card-back .brand-name { color: var(--on-grey); left: 0; width: 665px; top: 196px; font-size: 32px; letter-spacing: 4px; }
  .card-back .brand-tagline { color: var(--on-grey); left: 0; width: 665px; top: 252px; font-size: 18px; letter-spacing: 6px; }
  .back-web { position: absolute; left: 0; width: 665px; top: 345px; margin: 0; text-align: center; font-family: "Crimson Text", serif; font-size: 17px; letter-spacing: 1px; color: var(--on-grey); }
</style>
</head>
<body>
  <section class="card card-front">
    <div class="brand-mark"></div>
    <p class="brand-name">Colby Varnway</p>
    <p class="brand-tagline">Photographers</p>
    <div class="divider"></div>
    <div class="contact">
      <h2 class="contact-name">Colby Varnway</h2>
      <ul class="contact-list">
        <li><svg viewBox="0 0 12 12" aria-hidden="true"><path d="M3 1 L5 3.5 L4 5 Q5.5 7.5 7 8 L8.5 7 L11 9 L9.5 11 Q4 10.5 1 3 Z"/></svg>5208813047</li>
        <li><svg viewBox="0 0 12 12" aria-hidden="true"><path d="M0 2h12v8H0z M1 3 L6 6.5 L11 3 V3.2 L6 7.5 L1 3.2 Z" fill-rule="evenodd"/></svg>colby@colbyvarnway.com</li>
        <li><svg viewBox="0 0 12 12" aria-hidden="true"><path d="M6 .5a5.5 5.5 0 1 0 0 11a5.5 5.5 0 1 0 0-11zm0 1a4.5 4.5 0 1 1 0 9a4.5 4.5 0 1 1 0-9zM1.5 5.5h9v1h-9zM5.5 1h1v10h-1z"/></svg>www.colbyvarnway.com</li>
        <li class="social"><svg viewBox="0 0 12 12" aria-hidden="true"><rect x="1" y="1" width="10" height="10"/></svg>colbyvarnwayphoto</li>
      </ul>
    </div>
    <div class="front-band"></div>
  </section>

  <section class="card card-back">
    <div class="brand-mark"></div>
    <p class="brand-name">Colby Varnway</p>
    <p class="brand-tagline">Photographers</p>
    <p class="back-web">www.colbyvarnway.com</p>
  </section>
</body>
</html>
```